Lynx Payments Business card refresh

Need a new design of our business card The info is not what is on these cards i sent this for a reference. I can email all the info over
Info would be Colin Hadley Chief LYNX is the title. our new address is 47615 Birchmoor Ln. Sable Ridge Or 93058 Cell number is 805-462-3179 Work number is 855-307-4926 ext 347 Colin@lynxpaysample.com is my email address
Target Market(s)
Merchant Services all businesses that take credit cards
Industry/Entity Type
Merchant Services / Credit Card processing
Contact Information for Business Card
Need a new design of our business card The info is not what is on these cards i sent this for a reference. I can email all the info over Info would be Colin Hadley Chief LYNX is the title. our new address is 47615 Birchmoor Ln. Sable Ridge Or 93058 Cell number is 805-462-3179 Work number is 855-307-4926 ext 347 Colin@lynxpaysample.com is my email address
Requirements
Must have
- My logo and colors from my brand guidelines
Nice to have
- i sent some designs just need a new refresh
Should not have
- nothing specific

```html
<!DOCTYPE html>
<html lang="en">
<head>
<meta charset="utf-8">
<title>Lynx Payments – Business Card</title>
<link href="https://fonts.googleapis.com/css2?family=Raleway:wght@400;500;700;800&display=swap" rel="stylesheet">
<style>
  :root {
    --brand-green: #9bc400;
    --card-white: #ffffff;
    --card-dark: #2b3036;
    --ink: #1e1e1e;
    --backdrop: #3b3b3d;
  }
  * { box-sizing: border-box; margin: 0; padding: 0; }
  html, body {
    width: 1200px; height: 1200px; overflow: hidden;
    background: var(--backdrop);
    font-family: 'Raleway', sans-serif;
  }
  .card {
    position: absolute;
    left: 250px;
    width: 700px; height: 400px;
    border-radius: 30px;
    box-shadow: 0 4px 0 var(--brand-green), 0 18px 40px rgba(0,0,0,.45);
    overflow: hidden;
  }
  .card--front { top: 140px; background: var(--card-white); }
  .card--back  { top: 650px; background: var(--card-dark); }

  /* front */
  .front-brand {
    position: absolute; left: 60px; bottom: 40px;
    display: flex; align-items: center; gap: 16px;
  }
  .front-brand__square { width: 34px; height: 34px; background: var(--brand-green); }
  .front-brand__name {
    font-weight: 800; font-size: 40px; color: var(--brand-green);
  }
  .contact {
    position: absolute; left: 372px; top: 80px; color: var(--ink);
  }
  .contact__name {
    font-weight: 800; font-size: 31px; color: var(--brand-green);
    letter-spacing: -0.5px; line-height: 1;
  }
  .contact__title {
    font-weight: 500; font-size: 15px; letter-spacing: 0.5px;
    margin-top: 3px; margin-bottom: 20px;
  }
  .contact__title strong { font-weight: 800; }
  .contact__list { list-style: none; }
  .contact__item {
    display: flex; align-items: flex-start; gap: 12px;
    font-size: 17px; font-weight: 500; line-height: 24px;
  }
  .contact__icon { width: 16px; height: 24px; flex: none; fill: var(--brand-green); }

  /* back */
  .back-brand {
    position: absolute; inset: 0;
    display: flex; align-items: center; justify-content: center; gap: 22px;
  }
  .back-brand__circle {
    width: 44px; height: 44px; border-radius: 50%; background: var(--brand-green);
  }
  .back-brand__name {
    font-weight: 800; font-size: 64px; color: #f2f2f2; letter-spacing: 1px;
  }
</style>
</head>
<body>

<section class="card card--front" aria-label="Business card front">
  <div class="front-brand">
    <span class="front-brand__square"></span>
    <span class="front-brand__name">Lynx Payments</span>
  </div>

  <div class="contact">
    <div class="contact__name">COLIN HADLEY</div>
    <div class="contact__title">CHIEF <strong>LYNX</strong></div>
    <ul class="contact__list">
      <li class="contact__item">
        <svg class="contact__icon" viewBox="0 0 16 24" aria-hidden="true"><path d="M4 3h8a2 2 0 0 1 2 2v14a2 2 0 0 1-2 2H4a2 2 0 0 1-2-2V5a2 2 0 0 1 2-2zm0 3v11h8V6zm4 12.2a1 1 0 1 0 0 .1z"/></svg>
        805-462-3179
      </li>
      <li class="contact__item">
        <svg class="contact__icon" viewBox="0 0 16 24" aria-hidden="true"><path d="M3.5 6l3 3-1.6 1.8a10 10 0 0 0 4.3 4.3L11 13.5l3 3-2 2.5C6.5 18.5 1.5 13.5 1 8z"/></svg>
        855-307-4926 ext 347
      </li>
      <li class="contact__item">
        <svg class="contact__icon" viewBox="0 0 16 24" aria-hidden="true"><path d="M0 7h16v11H0zm1.5 1.5L8 13l6.5-4.5z"/></svg>
        Colin@lynxpaysample.com
      </li>
      <li class="contact__item">
        <svg class="contact__icon" viewBox="0 0 16 24" aria-hidden="true"><path d="M8 3a6 6 0 0 1 6 6c0 4.5-6 12-6 12S2 13.5 2 9a6 6 0 0 1 6-6zm0 3.5a2.5 2.5 0 1 0 0 5 2.5 2.5 0 0 0 0-5z"/></svg>
        <span>47615 Birchmoor Ln.<br>Sable Ridge Or 93058</span>
      </li>
    </ul>
  </div>
</section>

<section class="card card--back" aria-label="Business card back">
  <div class="back-brand">
    <span class="back-brand__circle"></span>
    <span class="back-brand__name">Lynx Payments</span>
  </div>
</section>

</body>
</html>
```